Brightpath Medical Exercise, LLC specializes in post rehab medical exercise for clients who have been discharged from physical therapy and/or other medical services and are in need of continued cardiovascular, strength, flexibility, endurance training and management of their medical conditions. We strive to bridge the gap between healthcare and fitness by staying in communication with the referring physician and /or physical therapist with updated progress notes to follow each clients progression, making sure each client is appropriate for exercise and identifying any red flags throughout the initial assessment and screening of the client, and referring those clients back to the physician and/or therapist when necessary.
Colors
Designer to choose colors to be used in the design.
Requirements
Must have
- Pictures of a trainer working with a client one on one during exercise, and group exercise
Nice to have
- Pictures that portray the bridge between healthcare and fitness
Should not have
- Cursive writing

```html
<!DOCTYPE html>
<html lang="en">
<head>
<meta charset="utf-8">
<title>Brightpath Medical Exercise – Rack Card</title>
<link href="https://fonts.googleapis.com/css2?family=Montserrat:wght@500;700;800&family=Open+Sans:wght@400;600;700&display=swap" rel="stylesheet">
<style>
  :root{
    --red:#f0493f;
    --red-soft:#f76a5c;
    --ink:#1c1c1e;
    --black:#161616;
    --grey-bg:#e6e6e8;
    --white:#ffffff;
    --text:#222;
  }
  *{box-sizing:border-box;margin:0;padding:0}
  html,body{width:1200px;height:1177px;overflow:hidden;background:var(--grey-bg)}
  body{position:relative;font-family:"Open Sans",Arial,sans-serif;color:var(--text)}
  .rack-card{position:absolute;left:290px;top:28px;width:620px;height:1120px;background:var(--white);overflow:hidden;box-shadow:0 6px 24px rgba(0,0,0,.18)}
  .hero-photo{position:absolute;left:0;top:0;width:620px;height:480px;
    background:linear-gradient(120deg,#9a9590 0%,#d9c2b0 40%,#efe2d6 65%,#f4f1ee 100%)}
  .hero-curve{position:absolute;left:0;top:360px;width:620px;height:150px}
  .brand-badge{position:absolute;left:48px;top:300px;width:206px;height:206px;border-radius:50%;
    background:radial-gradient(circle at 40% 35%,var(--red-soft),var(--red) 70%);
    border:8px solid var(--white);box-shadow:0 0 0 4px var(--black);
    display:flex;align-items:center;justify-content:center;text-align:center}
  .brand-badge .brand-name{font-family:"Montserrat",sans-serif;font-weight:700;font-size:15px;line-height:1.25;color:var(--white);letter-spacing:.5px}
  .services{position:absolute;left:30px;right:30px;top:534px;text-align:center}
  .services h2{font-family:"Montserrat",sans-serif;font-weight:800;font-size:15px;color:var(--red);letter-spacing:.3px}
  .services ul{list-style:none;font-size:11.5px;line-height:1.6;margin-top:4px}
  .services li{display:inline-block;margin:0 8px}
  .services li::before,.conditions li::before{content:"";display:inline-block;width:6px;height:6px;border-radius:50%;background:var(--red);margin-right:6px;vertical-align:middle}
  .divider{position:absolute;left:70px;right:70px;top:614px;border-top:1.5px solid #444}
  .quote{position:absolute;left:20px;right:20px;top:626px;text-align:center;font-family:"Montserrat",sans-serif;font-weight:800;font-size:15px;line-height:1.25;color:var(--red);text-transform:uppercase}
  .intro{position:absolute;left:20px;right:20px;top:669px;text-align:center;font-size:15px;color:var(--red)}
  .conditions{position:absolute;top:712px;list-style:none;font-weight:700;font-size:12.5px;line-height:23px;color:var(--ink);white-space:nowrap}
  .conditions.col-1{left:30px}
  .conditions.col-2{left:214px}
  .conditions.col-3{left:414px}
  .weights-photo{position:absolute;left:30px;top:900px;width:110px;height:80px;border-radius:10px;
    background:linear-gradient(135deg,#3a5bbf,#1c2f7a)}
  .footer-shape{position:absolute;left:0;top:900px;width:620px;height:220px}
  .footer{position:absolute;left:0;right:0;bottom:0;height:130px;color:var(--white)}
  .phone{position:absolute;left:30px;top:14px;font-family:"Montserrat",sans-serif;font-weight:700;font-size:27px;display:flex;align-items:center;gap:10px}
  .phone svg{width:26px;height:26px}
  .contact{position:absolute;left:330px;top:4px;list-style:none;font-size:18px;line-height:30px}
  .contact li{display:flex;align-items:center;gap:10px}
  .contact svg{width:18px;height:18px;flex:none}
  .tagline{position:absolute;left:30px;right:20px;bottom:16px;font-size:10.5px;letter-spacing:.2px}
</style>
</head>
<body>
<article class="rack-card">
  <div class="hero-photo" role="img" aria-label="Photo of a trainer guiding a client through a resistance band exercise"></div>

  <svg class="hero-curve" viewBox="0 0 620 150" preserveAspectRatio="none" aria-hidden="true">
    <path d="M0 150 L0 110 Q300 140 620 40 L620 150 Z" fill="var(--white)"/>
    <path d="M200 150 Q420 130 620 60 L620 90 Q430 150 250 150 Z" fill="var(--black)"/>
    <path d="M0 108 Q300 138 620 38" fill="none" stroke="var(--red)" stroke-width="5"/>
  </svg>

  <div class="brand-badge"><span class="brand-name">BRIGHTPATH<br>MEDICAL EXERCISE</span></div>

  <section class="services">
    <h2>OUR PRODUCTS AND SERVICES:</h2>
    <ul>
      <li>Initial Assessment and Functional Screening</li>
      <li>One-On-One supervised post rehab exercise</li>
      <li>Online consultation with individualized home exercise program</li>
    </ul>
  </section>
  <div class="divider"></div>

  <p class="quote">“Exercise is the key to long-term management of most medical conditions” ~ Daniel R. Hayes, PhD, PT</p>
  <p class="intro">We offer management of the following conditions and more</p>

  <ul class="conditions col-1">
    <li>Diabetes</li><li>Bicipital Tendonitis</li><li>Spinal Stenosis</li><li>Scoliosis</li><li>AC Joint Separation</li><li>Parkinson’s Disease</li><li>Carpal Tunnel Syndrome</li><li>Bicipital Tendonitis</li><li>Cervical Strain</li>
  </ul>
  <ul class="conditions col-2">
    <li>Hypertension</li><li>ACL Rupture</li><li>Total Hip Replacement</li><li>Multiple Sclerosis</li><li>Osteoporosis</li><li>Fibromyalgia</li><li>Osteoarthritis</li><li>Tibial Plateau Fracture</li><li>Total Shoulder Replacement</li>
  </ul>
  <ul class="conditions col-3">
    <li>Patello-Femoral Syndrome</li><li>Impingement Syndrome</li><li>Ankle Fracture</li><li>Total Knee Replacement</li><li>Shoulder Dislocation</li><li>Cervical disc herniation</li><li>Spondylothesis</li><li>Tennis Elbow/Golfer’s Elbow</li><li>Rotator Cuff Syndrome</li><li>Laminectomy</li>
  </ul>

  <svg class="footer-shape" viewBox="0 0 620 220" preserveAspectRatio="none" aria-hidden="true">
    <path d="M0 40 Q90 20 170 120 L0 120 Z" fill="var(--red)"/>
    <path d="M0 120 Q300 60 620 95 L620 220 L0 220 Z" fill="var(--black)"/>
    <path d="M0 118 Q300 58 620 93" fill="none" stroke="var(--red)" stroke-width="3"/>
  </svg>
  <div class="weights-photo" role="img" aria-label="Photo of blue hand dumbbells"></div>

  <footer class="footer">
    <div class="phone">
      <svg viewBox="0 0 24 24"><rect x="1" y="1" width="22" height="22" rx="4" fill="#fff"/><path d="M8 5c-1 1-2 2-1 5s3 6 6 8 4 0 5-1l-2-3-2 1c-1 0-3-2-4-4l1-2z" fill="var(--black)"/></svg>
      (555) 014-2236
    </div>
    <ul class="contact">
      <li><svg viewBox="0 0 24 24" fill="none" stroke="#fff" stroke-width="1.8"><path d="M12 22s7-7 7-12a7 7 0 0 0-14 0c0 5 7 12 7 12z"/><circle cx="12" cy="10" r="2.5"/></svg>Riverton, GA, USA</li>
      <li><svg viewBox="0 0 24 24" fill="none" stroke="#fff" stroke-width="1.8"><rect x="2" y="5" width="20" height="14"/><path d="M2 5l10 8 10-8"/></svg>brightpathmedex@mail.com</li>
      <li><svg viewBox="0 0 24 24" fill="none" stroke="#fff" stroke-width="1.8"><circle cx="12" cy="12" r="10"/><path d="M2 12h20M12 2c3 3 3 17 0 20M12 2c-3 3-3 17 0 20"/></svg>www.brightpathmedex.com</li>
    </ul>
    <p class="tagline">BRIGHTPATH MEDICAL EXERCISE, LLC &nbsp;“Getting You Back To Function As Quickly And Safely As Possible”</p>
  </footer>
</article>
</body>
</html>
```